BrightPath Medical Exercise, LLC specializes in post rehab medical exercise for clients who have been discharged from physical therapy and/or other medical services and are in need of continued cardiovascular, strength, flexibility, endurance training and management of their medical conditions. We strive to bridge the gap between healthcare and fitness by staying in communication with the referring physician and /or physical therapist with updated progress notes to follow each clients progression, making sure each client is appropriate for exercise and identifying any red flags throughout the initial assessment and screening of the client, and referring those clients back to the physician and/or therapist when necessary.
Colors
Designer to choose colors to be used in the design.
Requirements
Must have
- Pictures of a trainer working with a client one on one during exercise, and group exercise
Nice to have
- Pictures that portray the bridge between healthcare and fitness
Should not have
- Cursive writing

```html
<!DOCTYPE html>
<html lang="en">
<head>
<meta charset="utf-8">
<title>BrightPath Medical Exercise – Rack Card</title>
<link rel="stylesheet" href="https://fonts.googleapis.com/css2?family=Playfair+Display:wght@400&family=Jost:wght@400;500&display=swap">
<style>
  :root {
    --orange: #ee4a2c;
    --orange-deep: #d93a20;
    --black: #0d0d0d;
    --charcoal: #2a2a2a;
    --white: #ffffff;
    --page: #e6e6e4;
    --ink: #333333;
  }
  * { box-sizing: border-box; margin: 0; padding: 0; }
  html, body { width: 1200px; height: 688px; overflow: hidden; }
  body { background: var(--page); position: relative; font-family: "Jost", sans-serif; }

  .card {
    position: absolute;
    top: 29px;
    width: 280px;
    height: 630px;
    overflow: hidden;
    box-shadow: 0 6px 18px rgba(0,0,0,.25);
  }
  .card--front { left: 250px; background: var(--white); }
  .card--back { left: 670px; background: var(--orange); }

  .card__shapes { position: absolute; inset: 0; width: 280px; height: 630px; }
  .layer { position: absolute; }

  /* Front */
  .brand {
    position: absolute; left: 18px; top: 36px; width: 100px;
    display: flex; flex-direction: column; align-items: center; gap: 8px;
  }
  .brand__dot { width: 56px; height: 56px; border-radius: 50%; background: var(--orange); }
  .brand__name {
    font-family: "Jost", sans-serif; font-weight: 500; font-size: 8px;
    letter-spacing: .3px; text-transform: uppercase; color: var(--ink);
    text-align: center; line-height: 1.25;
  }
  .headline {
    position: absolute; left: 0; top: 480px; width: 280px;
    text-align: center; color: var(--white);
    font-family: "Playfair Display", serif; font-size: 19px; line-height: 24px;
  }
  .headline__accent { color: var(--orange); font-size: 29px; line-height: 32px; }
  .headline__joiner { font-size: 20px; color: var(--white); }

  /* Back */
  .section-title {
    position: absolute; left: 40px; top: 22px; width: 200px;
    text-align: center; color: var(--white);
    font-family: "Playfair Display", serif; font-size: 18px; line-height: 20px;
  }
  .services {
    position: absolute; left: 24px; top: 88px; width: 250px;
    list-style: none; color: var(--white);
    font-family: "Playfair Display", serif; font-size: 10.5px; line-height: 12.5px;
  }
  .services li { padding-left: 9px; position: relative; }
  .services li::before {
    content: ""; position: absolute; left: 0; top: 4px;
    width: 5px; height: 5px; border-radius: 50%; background: var(--white);
  }
  .quote {
    position: absolute; left: 10px; top: 367px; width: 260px;
    text-align: center; font-family: "Playfair Display", serif;
    font-size: 10.5px; line-height: 12.5px; color: var(--black);
  }
  .quote__author { display: block; color: var(--orange); font-size: 11px; }
  .conditions-intro {
    position: absolute; left: 10px; top: 410px; width: 260px;
    text-align: center; font-family: "Playfair Display", serif;
    font-size: 11px; line-height: 13px; color: var(--white);
  }
  .conditions {
    position: absolute; left: 14px; top: 452px; width: 260px;
    display: flex; gap: 10px;
  }
  .conditions ul {
    list-style: none; color: var(--white);
    font-family: "Jost", sans-serif; font-size: 7.6px; line-height: 10.8px;
  }
  .conditions ul:first-child { width: 118px; }
  .conditions li { padding-left: 6px; position: relative; white-space: nowrap; }
  .conditions li::before {
    content: ""; position: absolute; left: 0; top: 4px;
    width: 3px; height: 3px; border-radius: 50%; background: var(--white);
  }
</style>
</head>
<body>

<section class="card card--front" aria-label="Rack card front">
  <svg class="card__shapes" viewBox="0 0 280 630" aria-hidden="true">
    <defs>
      <linearGradient id="trainingPhotoTone" x1="0" y1="0" x2="1" y2="1">
        <stop offset="0" stop-color="#f3ece6"/>
        <stop offset=".55" stop-color="#e2cbbb"/>
        <stop offset="1" stop-color="#bfd9cf"/>
      </linearGradient>
      <linearGradient id="equipmentPhotoTone" x1="0" y1="0" x2="0" y2="1">
        <stop offset="0" stop-color="#7c8c9a"/>
        <stop offset="1" stop-color="#b89a78"/>
      </linearGradient>
    </defs>
    <rect x="112" y="0" width="168" height="470" fill="url(#trainingPhotoTone)"/>
    <polygon points="0,272 150,420 280,270 280,630 0,630" fill="var(--black)"/>
    <polygon points="280,270 280,430 190,430" fill="var(--charcoal)"/>
    <polygon points="0,272 150,420 110,420" fill="var(--charcoal)"/>
    <polygon points="89,297 179,387 89,477 -1,387" fill="var(--white)"/>
    <polygon points="0,560 0,630 46,630" fill="var(--orange)"/>
    <polygon points="280,520 280,630 180,630" fill="var(--orange)"/>
  </svg>
  <div class="layer" role="img" aria-label="Photo of a woman doing resistance band exercise with a trainer's hands on her shoulders" style="left:112px;top:0;width:168px;height:270px;"></div>
  <svg class="card__shapes" viewBox="0 0 280 630" role="img" aria-label="Photo of blue dumbbells and a water bottle on a wooden floor">
    <polygon points="89,305 171,387 89,469 7,387" fill="url(#equipmentPhotoTone)"/>
  </svg>

  <div class="brand">
    <span class="brand__dot"></span>
    <span class="brand__name">BrightPath Medical Exercise</span>
  </div>

  <h1 class="headline">
    Getting You<br>
    Back To Function As<br>
    <span class="headline__accent">Quickly</span> <span class="headline__joiner">and</span> <span class="headline__accent">Safely</span><br>
    As Possible
  </h1>
</section>

<section class="card card--back" aria-label="Rack card back">
  <svg class="card__shapes" viewBox="0 0 280 630" aria-hidden="true">
    <defs>
      <linearGradient id="coachingPhotoTone" x1="0" y1="0" x2="1" y2="1">
        <stop offset="0" stop-color="#c9b3a2"/>
        <stop offset=".5" stop-color="#e6d6c8"/>
        <stop offset="1" stop-color="#9aa59c"/>
      </linearGradient>
    </defs>
    <polygon points="0,0 280,0 140,100" fill="var(--black)"/>
    <rect x="0" y="250" width="280" height="158" fill="var(--black)"/>
    <polygon points="0,360 140,240 280,360 280,408 0,408" fill="var(--white)"/>
    <rect x="0" y="408" width="280" height="40" fill="var(--black)"/>
    <polygon points="140,124 248,232 140,340 32,232" fill="var(--white)"/>
    <polygon points="280,555 280,630 205,630" fill="var(--black)"/>
  </svg>
  <svg class="card__shapes" viewBox="0 0 280 630" role="img" aria-label="Photo of a trainer coaching a client one on one in the gym">
    <polygon points="140,134 238,232 140,330 42,232" fill="url(#coachingPhotoTone)"/>
  </svg>

  <h2 class="section-title">Our Products and Services:</h2>
  <ul class="services">
    <li>Initial Assessment and Functional Screening</li>
    <li>One-On-One supervised post rehab exercise</li>
    <li>Online consultation with individualized home exercise program</li>
  </ul>

  <p class="quote">
    Exercise is the key to long-term management of<br>most medical conditions
    <span class="quote__author">Daniel R Hayes (PhD, PT)</span>
  </p>

  <p class="conditions-intro">We offer management of the following<br>conditions and more:</p>

  <div class="conditions">
    <ul>
      <li>Diabetes</li>
      <li>AC Joint Separation</li>
      <li>Hypertension</li>
      <li>Fibromyalgia</li>
      <li>ACL Rupture</li>
      <li>Spondylothesis</li>
      <li>Ankle Fracture</li>
      <li>Parkinson's Disease</li>
      <li>Bicipital Tendonitis</li>
      <li>Tibial Plateau Fracture</li>
      <li>Total Hip Replacement</li>
      <li>Tennis Elbow/Golfer's Elbow</li>
      <li>Total Knee Replacement</li>
      <li>Carpal Tunnel Syndrome</li>
    </ul>
    <ul>
      <li>Spinal Stenosis</li>
      <li>Total Shoulder Replacement</li>
      <li>Multiple Sclerosis</li>
      <li>Bicipital Tendonitis</li>
      <li>Shoulder Dislocation</li>
      <li>Patello-Femoral Syndrome</li>
      <li>Scoliosis Rotator Cuff Syndrome</li>
      <li>Osteoporosis</li>
      <li>Cervical Strain</li>
      <li>Osteoarthritis</li>
      <li>Impingement Syndrome</li>
      <li>Cervical disc herniation</li>
      <li>Laminectomy</li>
    </ul>
  </div>
</section>

</body>
</html>
```